Carte d'affaire bilingue

Nous avons besoin d'une carte d'affaire pour notre entreprise spécialisée en vente et achat de terrain. Nous sommes une agence immobilière et nous voulons une carte avec le recto en Français et le verso en anglais. Nous voulons une image sobre et épurée. Nous avons de la clientèle internationale et nous voulons une carte très professionnelle mais qui se démarque. Nous voulons cibler une clientèle commerciale, industrielle, contracteurs et promoteurs immobiliers.
Updates

Hi everybody, we saw all your conception and we are approching of what we like but the "WOW" is missing.

We love the little sign to specify (phone or email) but we can put them in a square to make like our logo, we love also dark gray not lite gray, we also love the stainless lines. In our logo you can see a little sign +. For us is signyfy " Always further" so if you can put many little +++++ in the conception somewhere very discret it will be appreciate. We also like a kind of round that make a magnyfying glass, because we search land we found opportunity.

Thank you

Reason: I ask different things in the last day but no one do what i am asking for. For the conception # 3016702 that we love we ask changes.

We like simplicity, urban design, corporate, international. The card must have one side in french and the other side in english. We like dark gray,silver, and a little bit of green.

Target Market(s)

Investors, developers, construction builders, etc...

Font styles to use
Serif
Sans Serif

Requirements
Must have
• logo
La mention: Agence immobilière (Francais) / Real Estate Agency (anglais)
Sous le nom: Courtier immobilier agréé (Français) / Real Estate Broker

```html
<!DOCTYPE html>
<html lang="fr">
<head>
<meta charset="utf-8">
<title>Le Repère Foncier – Carte d'affaire</title>
<link rel="stylesheet" href="https://fonts.googleapis.com/css2?family=Alegreya:wght@400&display=swap">
<style>
  :root {
    --ink: #323b3e;
    --ink-soft: #4a5457;
    --silver-light: #ffffff;
    --silver-mid: #d7dbdb;
    --silver-dark: #a3abab;
    --green: #168a10;
    --green-dark: #0c6f06;
    --green-light: #2fb21e;
    --divider: #65777a;
    --rule: #9aa3a4;
  }
  * { margin: 0; padding: 0; box-sizing: border-box; }
  html, body { width: 1009px; height: 1200px; overflow: hidden; background: var(--divider); }
  body { font-family: "Alegreya", Georgia, serif; color: var(--ink); }
  .sheet { position: relative; width: 1009px; height: 1200px; }
  .card {
    position: absolute; left: 0; width: 1009px; height: 591px; overflow: hidden;
    background: linear-gradient(160deg, var(--silver-light) 0%, var(--silver-mid) 45%, var(--silver-dark) 100%);
  }
  .card--front { top: 0; }
  .card--back { top: 609px; }
  .card__wave { position: absolute; inset: 0; width: 100%; height: 100%; }
  .brand-square {
    position: absolute; left: 52px; top: 48px; width: 150px; height: 150px;
    background: var(--green);
  }
  .brand-name {
    position: absolute; left: 232px; top: 38px;
    font-variant: small-caps; font-weight: 400; color: var(--ink);
    font-size: 92px; line-height: 104px; letter-spacing: 2px;
  }
  .brand-rule {
    position: absolute; left: 155px; top: 262px; width: 748px; height: 3px;
    background: var(--rule);
  }
  .tagline {
    position: absolute; left: 752px; top: 165px;
    font-size: 24px; line-height: 27px; letter-spacing: 2px; color: var(--ink-soft);
    list-style: none;
  }
  .mentions {
    position: absolute; left: 51px; top: 294px;
    font-size: 26px; line-height: 37px; color: var(--ink-soft); letter-spacing: 0.3px;
  }
</style>
</head>
<body>
<main class="sheet">

  <section class="card card--front" lang="fr">
    <svg class="card__wave" viewBox="0 0 1009 591" preserveAspectRatio="none" aria-hidden="true">
      <defs>
        <linearGradient id="waveFr" x1="0" y1="1" x2="1" y2="0">
          <stop offset="0" stop-color="#2aa51a"/>
          <stop offset="0.5" stop-color="#168a10"/>
          <stop offset="1" stop-color="#0c7a06"/>
        </linearGradient>
      </defs>
      <path d="M0,591 C70,520 190,475 400,462 C650,445 850,420 935,265 C990,160 1000,60 1009,0 L1009,591 Z" fill="url(#waveFr)"/>
    </svg>
    <div class="brand-square"></div>
    <h1 class="brand-name">Le Repère<br>Foncier</h1>
    <div class="brand-rule"></div>
    <ul class="tagline"><li>Explorer</li><li>Optimiser</li><li>Développer</li></ul>
    <p class="mentions">Courtier immobilier agréé (Français) / Real Estate Broker<br>Agence immobilière (Francais) / Real Estate Agency (anglais)</p>
  </section>

  <section class="card card--back" lang="en">
    <svg class="card__wave" viewBox="0 0 1009 591" preserveAspectRatio="none" aria-hidden="true">
      <defs>
        <linearGradient id="waveEn" x1="0" y1="1" x2="1" y2="0">
          <stop offset="0" stop-color="#2aa51a"/>
          <stop offset="0.5" stop-color="#168a10"/>
          <stop offset="1" stop-color="#0c7a06"/>
        </linearGradient>
      </defs>
      <path d="M0,591 C70,520 190,475 400,462 C650,445 850,420 935,265 C990,160 1000,60 1009,0 L1009,591 Z" fill="url(#waveEn)"/>
    </svg>
    <div class="brand-square"></div>
    <h2 class="brand-name">Parcel<br>Point</h2>
    <div class="brand-rule"></div>
    <ul class="tagline"><li>Explore</li><li>Develop</li><li>Optimize</li></ul>
    <p class="mentions">Courtier immobilier agréé (Français) / Real Estate Broker<br>Agence immobilière (Francais) / Real Estate Agency (anglais)</p>
  </section>

</main>
</body>
</html>
```